galactic arcade 80s vibes - jewelry company

I am looking for someone to build me a website for my jewelry company - I am going for an 80s retro GALACTIC arcade vibe. I want it to feel old school, be brightly colored (purples, greens, etc) encompass planets, stars, or milky way type vibes. My company is called LumoKitt - it is zodiac signs & angel number jewelry. I want the website to open up as galaxy and my logo/name to pop up in the center of the screen and then go to the main page.

Industry/Entity Type

jewelry

Coding

Coded - Design and coding required

Number of Pages Required

1 page

Font styles to use
Other font styles liked:
• retro

Colors
0094D4
00A9DD
6FCCEA
C7EBF8
E9F6FB
00AB8E
00BBA5
67D7C9
C6EFE9
E9F9F6
59FF00
82FF00
B8FF75
E3FFCB
F4FFEA
FFF300
FFF600
FEFA6F
FFFEC7
FFFEE8
FFC000
F8CF3A
FAE287
FDF2CF
FEFAEE
E54698
E96AAD
F1A4CE
F9D9EA
FCEFF6
A7469A
B969AE
D3A5CF
EDDBEB
F8F0F9
6B429C
8869AF
B7A5CE
E3DAEB
F3F0F8

```html
<!DOCTYPE html>
<html lang="en">
<head>
<meta charset="utf-8">
<title>LumoKitt — Zodiac & Angel Number Jewelry</title>
<link href="https://fonts.googleapis.com/css2?family=Lobster&family=Open+Sans:wght@400;600;700&display=swap" rel="stylesheet">
<style>
:root{
  --bg:#0b0b0d;
  --bg-soft:#141416;
  --white:#ffffff;
  --muted:#c9c9cf;
  --pink:#E54698;
  --pink-soft:#E96AAD;
  --purple:#A7469A;
  --violet:#6B429C;
  --green:#59FF00;
  --green-btn:#2fd12f;
  --yellow:#FFF300;
  --gold:#FFC000;
  --cyan:#00A9DD;
  --teal:#00BBA5;
}
*{box-sizing:border-box;margin:0;padding:0}
html,body{width:1200px;height:4280px;overflow:hidden;background:var(--bg)}
body{font-family:"Open Sans",sans-serif;color:var(--white);position:relative}
.script{font-family:"Lobster",cursive;font-weight:400}
.abs{position:absolute}
.photo{position:absolute}
.btn{position:absolute;display:flex;align-items:center;justify-content:center;font-size:14px;font-weight:600;color:#111;height:54px;width:168px}
.btn-green{background:var(--green-btn)}
.btn-yellow{background:var(--yellow)}
.star{position:absolute}
.dot{position:absolute;border-radius:50%}

/* brand name, plain text */
.brand{font-family:"Open Sans",sans-serif;font-weight:700;color:var(--white);letter-spacing:.5px}

/* nav */
.nav{position:absolute;top:0;left:0;width:1200px;height:90px;font-size:12px}
.nav-login{position:absolute;left:70px;top:18px;display:flex;align-items:center;gap:10px}
.social{width:14px;height:14px;border-radius:50%;background:var(--white)}
.nav-links{position:absolute;top:64px;left:360px;display:flex;gap:26px;font-size:12px}
.nav-links .active{color:var(--yellow)}
.nav-links .gap{width:110px}
.logo-nav{position:absolute;left:0;width:1200px;top:12px;text-align:center;font-size:28px;line-height:36px}
.nav-icons{position:absolute;right:70px;top:18px;display:flex;gap:18px}

/* hero */
.hero-title{left:88px;top:170px;width:640px;font-size:58px;line-height:1.35}
.hero-text{left:88px;top:370px;width:560px;font-size:15px;line-height:1.6;color:var(--muted)}

/* section titles */
.section-title{position:absolute;left:0;width:1200px;text-align:center;font-size:46px}

/* arrivals panel */
.promo{position:absolute;left:780px;top:900px;width:420px;height:400px;background:linear-gradient(160deg,var(--pink),var(--purple));padding:70px 40px}
.promo h3{font-size:38px;margin-bottom:14px}
.promo p{font-size:13px;line-height:1.6;width:300px}
.btn-outline{position:absolute;left:40px;top:270px;width:170px;height:54px;border:1px solid var(--white);display:flex;align-items:center;justify-content:center;font-size:14px}

/* about */
.about-text{left:88px;top:1570px;width:500px;font-size:15px;line-height:1.7;color:var(--muted)}

/* categories */
.tabs{position:absolute;left:680px;top:2070px;width:520px;height:34px;background:var(--pink);clip-path:polygon(6% 0,100% 0,100% 100%,0 100%);display:flex;align-items:center;gap:24px;padding-left:70px;font-size:11px}
.tabs .active{color:var(--yellow)}
.card{position:absolute;top:2180px;width:200px;height:300px;background:var(--white);color:#111}
.card .ring{position:absolute;left:30px;top:40px;width:140px;height:130px;background:radial-gradient(circle,#e6e6ee 20%,#b8b8c4 60%,#fff 75%)}
.badge{position:absolute;left:14px;top:12px;width:44px;height:44px;border-radius:50%;background:var(--purple);color:var(--white);font-size:11px;font-weight:700;display:flex;align-items:center;justify-content:center}
.heart{position:absolute;right:14px;top:14px}
.card .name{position:absolute;top:185px;left:0;width:100%;text-align:center;font-size:15px;font-weight:700}
.card .price{position:absolute;left:26px;top:222px;font-size:22px;font-weight:600}
.card .old{position:absolute;left:26px;top:256px;font-size:12px;color:#888;text-decoration:line-through}
.card .cart{position:absolute;right:20px;top:228px;width:90px;height:30px;background:var(--yellow);font-size:11px;font-weight:700;display:flex;align-items:center;justify-content:center}

/* sale */
.sale{position:absolute;left:390px;top:2570px;width:490px;height:450px;background:linear-gradient(180deg,var(--pink),var(--purple));text-align:center}
.sale h3{font-size:36px;color:var(--yellow);margin-top:40px}
.sale .off{margin:26px auto 0;width:360px;height:64px;background:var(--pink-soft);color:var(--yellow);font-size:38px;font-weight:700;display:flex;align-items:center;justify-content:center}
.countdown{display:flex;justify-content:center;gap:18px;margin-top:26px}
.count{display:flex;align-items:baseline;gap:6px;border-bottom:1px solid rgba(255,255,255,.5);padding-bottom:4px}
.count b{font-size:26px}
.count span{font-size:10px}
.sale .btn{left:145px;top:330px;width:200px}

/* blog */
.blog{position:absolute;top:3260px;width:300px}
.blog .img{width:300px;height:240px}
.blog p{margin-top:30px;font-size:16px;font-weight:700;line-height:1.5}
.blog .lead{color:var(--green)}

/* footer */
.footer{position:absolute;left:0;top:3780px;width:1200px;height:500px;background:var(--bg-soft)}
.logo-foot{position:absolute;left:0;width:1200px;top:48px;text-align:center;font-size:40px;line-height:52px}
.col{position:absolute;top:180px;font-size:13px}
.col h4{font-family:"Lobster",cursive;font-weight:400;font-size:19px;margin-bottom:26px}
.col li{list-style:none;margin-bottom:16px;color:var(--muted)}
.contact-row{display:flex;gap:12px;align-items:flex-start;margin-bottom:18px;color:var(--muted)}
.input{position:absolute;left:720px;top:250px;width:370px;height:60px;background:var(--white);color:#666;font-size:12px;padding:22px 20px}
.send{position:absolute;left:1010px;top:250px;width:80px;height:60px;background:var(--pink);display:flex;align-items:center;justify-content:center}
.foot-social{position:absolute;left:820px;top:340px;display:flex;gap:14px}
.foot-social div{width:24px;height:24px;border-radius:50%;border:1px solid var(--white)}
.copyright{position:absolute;left:0;top:4240px;width:1200px;height:40px;background:#050505;text-align:center;font-size:11px;line-height:40px;color:var(--muted)}
</style>
</head>
<body>

<!-- navigation -->
<header class="nav">
  <div class="nav-login">
    <svg width="16" height="16" viewBox="0 0 16 16"><circle cx="8" cy="5" r="3.5" fill="#fff"/><path d="M1 16c0-4 3-6 7-6s7 2 7 6z" fill="#fff"/></svg>
    <span style="margin-right:16px">Login</span>
    <div class="social"></div><div class="social"></div><div class="social"></div>
  </div>
  <div class="logo-nav brand">LumoKitt</div>
  <nav class="nav-links">
    <span class="active">Home</span><span>About Us</span><span>Product Categories</span>
    <span class="gap"></span>
    <span>New Arrival</span><span>Blog</span><span>Contact Us</span>
  </nav>
  <div class="nav-icons">
    <svg width="16" height="16" viewBox="0 0 16 16"><circle cx="7" cy="7" r="5" stroke="#fff" stroke-width="2" fill="none"/><path d="M11 11l4 4" stroke="#fff" stroke-width="2"/></svg>
    <svg width="16" height="16" viewBox="0 0 16 16"><path d="M8 14L2 8a3.3 3.3 0 016-4 3.3 3.3 0 016 4z" stroke="#fff" stroke-width="1.6" fill="none"/></svg>
    <svg width="16" height="16" viewBox="0 0 16 16"><path d="M1 2h3l2 8h8l2-6H5" stroke="#fff" stroke-width="1.6" fill="none"/><circle cx="7" cy="13.5" r="1.3" fill="#fff"/><circle cx="13" cy="13.5" r="1.3" fill="#fff"/></svg>
    <svg width="16" height="16" viewBox="0 0 16 16"><circle cx="8" cy="5" r="3.5" fill="#fff"/><path d="M1 16c0-4 3-6 7-6s7 2 7 6z" fill="#fff"/></svg>
  </div>
</header>

<!-- hero -->
<section class="hero">
  <div class="photo" role="img" aria-label="Model wearing a pearl necklace and earrings" style="left:760px;top:90px;width:400px;height:570px;background:radial-gradient(ellipse at 55% 40%,#c98f78 0%,#6a4436 45%,#161010 80%)"></div>
  <h1 class="abs script hero-title">The Perfect Jewels For You By LumoKitt</h1>
  <p class="abs hero-text">Lorem ipsum dolor sit amet, consectetur adipiscing elit. Condimentum pellentesque orci, id est suspendisse egestas leo. Nibh elementum nisi, eu quis vitae integer faucibus mi.</p>
  <div class="btn btn-green" style="left:88px;top:475px">Exlore More</div>
  <div class="btn btn-yellow" style="left:300px;top:475px">Buy Now</div>
</section>

<!-- decorative stars and dots -->
<svg class="star" style="left:30px;top:140px" width="30" height="30" viewBox="0 0 24 24"><path d="M12 1l3 8h8l-6.5 5 2.5 8-7-5-7 5 2.5-8L1 9h8z" fill="#A7469A"/></svg>
<div class="dot" style="left:60px;top:600px;width:16px;height:16px;background:var(--yellow)"></div>
<div class="dot" style="left:660px;top:530px;width:22px;height:22px;background:var(--teal)"></div>
<svg class="star" style="left:400px;top:1410px" width="32" height="32" viewBox="0 0 24 24"><path d="M12 1l3 8h8l-6.5 5 2.5 8-7-5-7 5 2.5-8L1 9h8z" fill="#A7469A"/></svg>
<div class="dot" style="left:630px;top:1410px;width:34px;height:34px;background:var(--yellow)"></div>
<div class="dot" style="left:-20px;top:1400px;width:52px;height:52px;background:var(--teal)"></div>
<svg class="star" style="left:40px;top:1860px" width="30" height="30" viewBox="0 0 24 24"><path d="M12 1l3 8h8l-6.5 5 2.5 8-7-5-7 5 2.5-8L1 9h8z" fill="#59FF00"/></svg>
<svg class="star" style="left:1140px;top:1430px" width="34" height="34" viewBox="0 0 24 24"><path d="M12 1l3 8h8l-6.5 5 2.5 8-7-5-7 5 2.5-8L1 9h8z" fill="none" stroke="#59FF00" stroke-width="1"/></svg>
<svg class="star" style="left:890px;top:2950px" width="34" height="34" viewBox="0 0 24 24"><path d="M12 1l3 8h8l-6.5 5 2.5 8-7-5-7 5 2.5-8L1 9h8z" fill="#E54698"/></svg>
<div class="dot" style="left:-20px;top:3100px;width:70px;height:70px;background:var(--green)"></div>
<div class="dot" style="left:80px;top:3110px;width:28px;height:28px;background:var(--pink)"></div>
<svg class="star" style="left:0px;top:3420px" width="60" height="60" viewBox="0 0 24 24"><path d="M12 1l3 8h8l-6.5 5 2.5 8-7-5-7 5 2.5-8L1 9h8z" fill="none" stroke="#FFC000" stroke-width=".6"/></svg>
<div class="dot" style="left:1040px;top:3140px;width:20px;height:20px;background:var(--gold)"></div>
<svg class="star" style="left:1030px;top:3610px" width="40" height="40" viewBox="0 0 24 24"><path d="M12 1l3 8h8l-6.5 5 2.5 8-7-5-7 5 2.5-8L1 9h8z" fill="#FFF300"/></svg>

<!-- new arrivals -->
<h2 class="section-title script" style="top:770px">New Arrivals</h2>
<div class="photo" role="img" aria-label="Woman wearing a delicate gold pendant necklace" style="left:0;top:900px;width:420px;height:400px;background:linear-gradient(135deg,#e9dcd2,#c7a592 60%,#f3ece6)"></div>
<div class="photo" role="img" aria-label="Pair of gold and diamond rings" style="left:432px;top:900px;width:336px;height:190px;background:linear-gradient(135deg,#f2f2f2,#cfcac0)"></div>
<div class="photo" role="img" aria-label="Rose gold bracelet on pink background" style="left:432px;top:1110px;width:336px;height:190px;background:linear-gradient(135deg,#f4c9c0,#e8a596)"></div>
<div class="promo">
  <h3 class="script">Aenean non</h3>
  <p>Lorem ipsum dolor sit amet, consectetur adipiscing elit. Egestas quis nisl enim neque turpis duis.</p>
  <div class="btn-outline">Buy Now</div>
</div>

<!-- about -->
<h2 class="abs script" style="left:88px;top:1470px;font-size:46px">About Us</h2>
<p class="abs about-text">Lorem ipsum dolor sit amet, consectetur adipiscing elit. Ultrices tempus nam eget pharetra in ac cursus consequat. Pharetra vitae integer erat porttitor cras placerat senectus diam consectetur. Velit pellentesque et massa risus. Eleifend tortor morbi non aliquam nunc, mattis facilisis suscipit. Malesuada sed porttitor tempor, amet in in. Auctor arcu at non risus, pharetra. Integer quam tellus quam et. Cras varius id tortor aliquam nunc eget.</p>
<div class="btn btn-yellow" style="left:88px;top:1800px">Exlore More</div>
<div class="abs" style="left:615px;top:1525px;width:585px;height:430px;background:var(--pink)"></div>
<div class="photo" role="img" aria-label="Woman wearing gold necklaces and bracelets" style="left:630px;top:1525px;width:570px;height:415px;background:linear-gradient(135deg,#8a9a4a,#5e6a30 45%,#c59a74 70%,#3b3020)"></div>

<!-- product categories -->
<h2 class="section-title script" style="top:2060px;left:-300px">Product Categories</h2>
<div class="tabs"><span class="active">All</span><span>Necklaces</span><span>Rings</span><span>Bracelets</span><span>Body Chains</span><span>Gem Sets</span></div>

<div class="card" style="left:-20px"><div class="ring" role="img" aria-label="Silver diamond ring"></div><div class="badge">-20%</div><svg class="heart" width="16" height="16" viewBox="0 0 16 16"><path d="M8 14L2 8a3.3 3.3 0 016-4 3.3 3.3 0 016 4z" stroke="#111" stroke-width="1.4" fill="none"/></svg><div class="name">Product Name Here</div><div class="price">$500</div><div class="old">$1000</div><div class="cart">Add To Cart</div></div>
<div class="card" style="left:205px"><div class="ring" role="img" aria-label="Silver diamond ring"></div><div class="badge">-20%</div><svg class="heart" width="16" height="16" viewBox="0 0 16 16"><path d="M8 14L2 8a3.3 3.3 0 016-4 3.3 3.3 0 016 4z" stroke="#111" stroke-width="1.4" fill="none"/></svg><div class="name">Product Name Here</div><div class="price">$500</div><div class="old">$1000</div><div class="cart">Add To Cart</div></div>
<div class="card" style="left:430px"><div class="ring" role="img" aria-label="Silver diamond ring"></div><div class="badge">-20%</div><svg class="heart" width="16" height="16" viewBox="0 0 16 16"><path d="M8 14L2 8a3.3 3.3 0 016-4 3.3 3.3 0 016 4z" stroke="#111" stroke-width="1.4" fill="none"/></svg><div class="name">Product Name Here</div><div class="price">$500</div><div class="old">$1000</div><div class="cart">Add To Cart</div></div>
<div class="card" style="left:655px"><div class="ring" role="img" aria-label="Silver diamond ring"></div><div class="badge">-20%</div><svg class="heart" width="16" height="16" viewBox="0 0 16 16"><path d="M8 14L2 8a3.3 3.3 0 016-4 3.3 3.3 0 016 4z" stroke="#111" stroke-width="1.4" fill="none"/></svg><div class="name">Product Name Here</div><div class="price">$500</div><div class="old">$1000</div><div class="cart">Add To Cart</div></div>
<div class="card" style="left:880px"><div class="ring" role="img" aria-label="Silver diamond ring"></div><div class="badge">-20%</div><svg class="heart" width="16" height="16" viewBox="0 0 16 16"><path d="M8 14L2 8a3.3 3.3 0 016-4 3.3 3.3 0 016 4z" stroke="#111" stroke-width="1.4" fill="none"/></svg><div class="name">Product Name Here</div><div class="price">$500</div><div class="old">$1000</div><div class="cart">Add To Cart</div></div>
<div class="card" style="left:1105px"><div class="ring" role="img" aria-label="Silver diamond ring"></div><div class="badge">-20%</div><svg class="heart" width="16" height="16" viewBox="0 0 16 16"><path d="M8 14L2 8a3.3 3.3 0 016-4 3.3 3.3 0 016 4z" stroke="#111" stroke-width="1.4" fill="none"/></svg><div class="name">Product Name Here</div><div class="price">$500</div><div class="old">$1000</div><div class="cart">Add To Cart</div></div>

<!-- sale -->
<div class="photo" role="img" aria-label="Hands wearing rings and a layered necklace" style="left:0;top:2600px;width:390px;height:420px;background:linear-gradient(135deg,#f4ece6,#d9b9a6 55%,#f0e4dc)"></div>
<div class="sale">
  <h3 class="script">Biggest Sale Is Here</h3>
  <div class="off">UPTO 50% OFF</div>
  <div class="countdown">
    <div class="count"><b>02</b><span>Days</span></div>
    <div class="count"><b>23</b><span>Hours</span></div>
    <div class="count"><b>20</b><span>Min</span></div>
    <div class="count"><b>42</b><span>Seconds</span></div>
  </div>
  <div class="btn btn-yellow">Exlore The Shop</div>
</div>
<div class="photo" role="img" aria-label="Rose gold ring with pink gemstone" style="left:810px;top:2600px;width:390px;height:395px;background:radial-gradient(circle at 50% 45%,#d26a9a 0%,#c99a7a 22%,#f5f2f0 45%)"></div>

<!-- blog -->
<h2 class="section-title script" style="top:3130px">Our Blog</h2>
<div class="blog" style="left:100px"><div class="img" role="img" aria-label="Diamond solitaire ring" style="background:linear-gradient(135deg,#ffffff,#d8d8dc)"></div><p class="lead">Lorem ipsum dolor sit amet, consectetur adipiscing elit. Diam.</p></div>
<div class="blog" style="left:450px"><div class="img" role="img" aria-label="Hands wearing gold rings and bracelets" style="background:linear-gradient(135deg,#6b4a3a,#c79a7c 55%,#3a2a22)"></div><p>Lorem ipsum dolor sit amet, consectetur adipiscing elit. Diam.</p></div>
<div class="blog" style="left:800px"><div class="img" role="img" aria-label="Gemstone rings arranged on a stone" style="background:linear-gradient(135deg,#f1ece6,#d7a86a 50%,#8fb9b0)"></div><p>Lorem ipsum dolor sit amet, consectetur adipiscing elit. Diam.</p></div>
<div class="btn btn-yellow" style="left:510px;top:3630px;width:180px">View All</div>

<!-- footer -->
<footer class="footer">
  <div class="logo-foot brand">LumoKitt</div>
  <div class="col" style="left:88px">
    <h4>Quick Links</h4>
    <ul><li>Home</li><li>About Us</li><li>Product Categories</li><li>Blog</li><li>New Arrival</li></ul>
  </div>
  <div class="col" style="left:355px">
    <h4>Contact Info</h4>
    <div class="contact-row"><svg width="14" height="14" viewBox="0 0 16 16"><path d="M3 1h3l1 4-2 1a9 9 0 005 5l1-2 4 1v3a2 2 0 01-2 2A13 13 0 011 3a2 2 0 012-2z" fill="#fff"/></svg><span>555.014.2290</span></div>
    <div class="contact-row"><svg width="14" height="14" viewBox="0 0 16 16"><path d="M8 0a5 5 0 015 5c0 4-5 11-5 11S3 9 3 5a5 5 0 015-5z" fill="#fff"/><circle cx="8" cy="5" r="2" fill="#141416"/></svg><span>12 Orbit Lane,<br>Star City 4021</span></div>
    <div class="contact-row"><svg width="14" height="14" viewBox="0 0 16 16"><rect x="1" y="3" width="14" height="10" fill="#fff"/><path d="M1 3l7 6 7-6" stroke="#141416" stroke-width="1.4" fill="none"/></svg><span>hello@lumokitt.example</span></div>
  </div>
  <div class="col" style="left:720px"><h4>Newsletter</h4></div>
  <div class="input">Email</div>
  <div class="send"><svg width="22" height="22" viewBox="0 0 24 24"><path d="M2 12L22 3l-6 19-4-8z" fill="#fff"/></svg></div>
  <div class="foot-social"><div></div><div></div><div></div></div>
</footer>
<div class="dot" style="left:1150px;top:3720px;width:40px;height:40px;background:var(--green)"></div>
<svg class="star" style="left:860px;top:3800px" width="30" height="30" viewBox="0 0 24 24"><path d="M12 1l3 8h8l-6.5 5 2.5 8-7-5-7 5 2.5-8L1 9h8z" fill="#6B429C"/></svg>
<svg class="star" style="left:250px;top:4180px" width="28" height="28" viewBox="0 0 24 24"><path d="M12 1l3 8h8l-6.5 5 2.5 8-7-5-7 5 2.5-8L1 9h8z" fill="#FFF300"/></svg>
<div class="copyright">© 2022 Jewelry Company, LLC</div>

</body>
</html>
```